Biodegradable box for eco-friendly bamboo cotton buds

I am looking for a design on a box holding 200 bamboo cotton buds. The box opens like a matchstick box and is made from recycled card. It's to sell online and at markets, maybe also supermarkets.
It's the second product my company, Verdalin, will sell, so I would like a design that I can replicate on other product packaging in the future.
You can see more about Verdalin on my website www.verdalin.org or facebook and instagram @verdalinqatar.
Please see below the box dimensions from the supplier and a photo. Also, some ideas I have had using Canva. I would like to see the green strip go all the way round the box. I like the font. The cotton bud logo is copyrighted - I like the style, but a new one would need to be created.

Target Market(s)

Eco-conscious consumers - expats and locals - in Qatar

Industry/Entity Type

Retail

Font styles to use
Other font styles liked:
• special elite

Colors
cadf82
acd037
eaf2ce
9ccb3b

Requirements
Must have
• an environmentally-friendly focus

```html
<!DOCTYPE html>
<html lang="en">
<head>
<meta charset="utf-8">
<title>Verdalin – Bamboo Cotton Buds box dieline</title>
<link rel="stylesheet" href="https://fonts.googleapis.com/css2?family=Special+Elite&family=Montserrat:wght@400;500&display=swap">
<style>
  :root {
    --ink: #111111;
    --paper: #ffffff;
    --strip-green: #1d8a1d;
    --lime: #7ee81c;
    --leaf-light: #eaf2ce;
    --leaf-mid: #cadf82;
    --leaf-deep: #9ccb3b;
  }
  html, body {
    margin: 0;
    padding: 0;
    width: 1200px;
    height: 864px;
    overflow: hidden;
    background: var(--paper);
  }
  .dieline-sheet {
    display: block;
    width: 1200px;
    height: 864px;
  }
  .cut { fill: none; stroke: var(--ink); stroke-width: 1.6; }
  .crop-mark { stroke: var(--ink); stroke-width: 1.2; fill: none; }
  .wrap-strip { fill: var(--strip-green); }
  .type-elite { font-family: "Special Elite", "Courier New", monospace; fill: var(--ink); }
  .type-sans { font-family: "Montserrat", Arial, sans-serif; fill: var(--ink); }
  .brand-name { font-family: "Montserrat", Arial, sans-serif; font-weight: 400; fill: var(--ink); }
  .tagline { font-size: 14px; }
  .product-title { font-size: 36px; text-anchor: middle; }
  .count-label { font-size: 21px; text-anchor: middle; font-weight: 500; }
  .count-rule { stroke: var(--lime); stroke-width: 3; }
  .claim-figure { font-size: 48px; fill: var(--lime); text-anchor: middle; }
  .claim-text { font-size: 23px; fill: var(--strip-green); text-anchor: middle; }
  .web-line { font-size: 21px; text-anchor: middle; }
  .social-handle { font-size: 18px; }
  .social-dot { fill: var(--ink); }
  .end-title { font-size: 36px; text-anchor: middle; }
  .end-count { font-size: 21px; text-anchor: middle; }
  .care-note { font-size: 12.5px; }
  .sleeve-brand { font-size: 50px; text-anchor: middle; }
</style>
</head>
<body>
<svg class="dieline-sheet" viewBox="0 0 2268 1632" xmlns="http://www.w3.org/2000/svg">
  <defs>
    <linearGradient id="bamboo-tones" x1="0" y1="0" x2="1" y2="1">
      <stop offset="0" stop-color="#f4f8e6"/>
      <stop offset="0.45" stop-color="#cadf82"/>
      <stop offset="0.75" stop-color="#acd037"/>
      <stop offset="1" stop-color="#eaf2ce"/>
    </linearGradient>
    <linearGradient id="bud-tones" x1="0" y1="0" x2="0" y2="1">
      <stop offset="0" stop-color="#9ccb3b"/>
      <stop offset="1" stop-color="#4d9a2a"/>
    </linearGradient>

    <!-- upper half of the tray dieline; mirrored for the lower half -->
    <g id="tray-half">
      <path class="cut" d="M612 115 L640 35 L1068 35 L1095 115"/>
      <rect class="cut" x="610" y="115" width="487" height="220"/>
      <path class="cut" d="M610 118 L458 118 L407 180 M407 132 L407 228 M407 132 L328 132 Q300 132 300 160 L300 306 Q300 335 328 335 L610 335"/>
      <path class="cut" d="M1097 118 L1248 118 L1300 180 M1300 132 L1300 228 M1300 132 L1380 132 Q1407 132 1407 160 L1407 306 Q1407 335 1380 335 L1097 335"/>
      <rect class="cut" x="589" y="335" width="529" height="27"/>
      <rect class="cut" x="589" y="362" width="529" height="224"/>
      <path class="cut" d="M589 367 L437 433 L367 586 M437 433 L589 586"/>
      <path class="cut" d="M1118 367 L1270 433 L1340 586 M1270 433 L1118 586"/>
    </g>

    <g id="crop-set-top">
      <path class="crop-mark" d="M116 0 V27 M335 0 V27 M361 0 V27 M586 0 V27 M1346 0 V27 M1372 0 V27 M1591 0 V27 M1672 0 V27 M1688 0 V27 M36 0 V27 M2232 0 V27"/>
      <path class="crop-mark" d="M1108 27 H1160 M1134 5 V27 M1122 27 A12 12 0 0 1 1146 27"/>
    </g>
    <g id="crop-set-left">
      <path class="crop-mark" d="M0 115 H27 M0 335 H27 M0 361 H27 M0 586 H27 M0 36 H27"/>
    </g>
  </defs>

  <!-- crop and registration marks -->
  <g class="crop-marks">
    <use href="#crop-set-top"/>
    <use href="#crop-set-top" transform="matrix(1 0 0 -1 0 1632)"/>
    <use href="#crop-set-left"/>
    <use href="#crop-set-left" transform="matrix(1 0 0 -1 0 1632)"/>
    <use href="#crop-set-left" transform="matrix(-1 0 0 1 2268 0)"/>
    <use href="#crop-set-left" transform="matrix(-1 0 0 -1 2268 1632)"/>
    <path class="crop-mark" d="M27 790 V842 M5 816 H27 M27 804 A12 12 0 0 0 27 828"/>
    <path class="crop-mark" d="M2241 790 V842 M2263 816 H2241 M2241 804 A12 12 0 0 1 2241 828"/>
  </g>

  <!-- tray dieline -->
  <g class="tray">
    <use href="#tray-half"/>
    <use href="#tray-half" transform="matrix(1 0 0 -1 0 1632)"/>

    <rect class="cut" x="335" y="586" width="1037" height="460" rx="14"/>
    <path class="cut" d="M361 586 V1046 M586 586 V1046 M1121 586 V1046 M1346 586 V1046"/>

    <rect class="cut" x="116" y="616" width="219" height="400"/>
    <path class="cut" d="M116 616 L35 642 L35 990 L116 1016"/>
    <rect class="cut" x="1372" y="616" width="219" height="400"/>
    <path class="cut" d="M1591 616 L1671 642 L1671 990 L1591 1016"/>

    <rect class="wrap-strip" x="1051" y="115" width="8" height="1401"/>
  </g>

  <!-- tray base: contact panel -->
  <g class="contact-panel">
    <text class="type-elite web-line" x="828" y="245">Find more products at verdalin.org</text>
    <circle class="social-dot" cx="758" cy="279" r="13"/>
    <text class="type-elite social-handle" x="790" y="285">@verdalinqatar</text>
  </g>

  <!-- front panel -->
  <g class="front-panel">
    <rect x="583" y="602" width="186" height="440" fill="url(#bamboo-tones)" opacity="0.85" role="img" aria-label="Hand-drawn bamboo stalks with leaves in soft greens"/>
    <text class="brand-name" x="915" y="716" font-size="34" text-anchor="middle">Verdalin</text>
    <text class="type-sans tagline" x="1005" y="736" text-anchor="end">Living lightly</text>
    <text class="type-elite product-title" x="920" y="812">Bamboo</text>
    <text class="type-elite product-title" x="920" y="847">Cotton Buds</text>
    <line class="count-rule" x1="822" y1="869" x2="872" y2="869"/>
    <text class="type-sans count-label" x="920" y="875">200 buds</text>
    <line class="count-rule" x1="968" y1="869" x2="1018" y2="869"/>
    <text class="type-elite claim-figure" x="918" y="962">100%</text>
    <text class="type-elite claim-text" x="918" y="988">Biodegrable</text>
    <text class="type-elite claim-text" x="920" y="1010">Buds &amp; Packaging</text>
  </g>

  <!-- left end panel -->
  <g class="end-panel-left">
    <text class="type-elite end-title" transform="translate(188 833) rotate(-90)">Bamboo</text>
    <text class="type-elite end-title" transform="translate(222 833) rotate(-90)">Cotton Buds</text>
    <text class="type-sans end-count" transform="translate(252 833) rotate(-90)">200 buds</text>
    <rect x="280" y="727" width="17" height="213" rx="8.5" fill="url(#bud-tones)" opacity="0.6" role="img" aria-label="Outline drawing of a single cotton bud"/>
  </g>

  <!-- right end panel: care notes -->
  <g class="end-panel-right type-elite care-note">
    <text transform="translate(1407 997) rotate(-90)" textLength="342" lengthAdjust="spacingAndGlyphs">Cotton buds have many uses, cleaning your ears is not one of them!</text>
    <text transform="translate(1441 997) rotate(-90)" textLength="362" lengthAdjust="spacingAndGlyphs">Ear wax is your ear's natural way of cleaning itself. Putting buds in</text>
    <text transform="translate(1459 997) rotate(-90)" textLength="248" lengthAdjust="spacingAndGlyphs">disrupts this process and damage the ear canal.</text>
    <text transform="translate(1493 997) rotate(-90)" textLength="292" lengthAdjust="spacingAndGlyphs">Never put anything smaller than your elbow in your ear!</text>
    <text transform="translate(1545 997) rotate(-90)" textLength="88" lengthAdjust="spacingAndGlyphs">Made in China</text>
    <text transform="translate(1560 997) rotate(-90)">CE</text>
  </g>

  <!-- outer sleeve -->
  <g class="sleeve">
    <path class="cut" d="M1688 115 L1710 35 L2207 35 L2233 115"/>
    <rect class="cut" x="1688" y="115" width="545" height="1383"/>
    <path class="cut" d="M1688 581 H2233 M1688 809 H2233 M1688 1275 H2233"/>
    <text class="brand-name sleeve-brand" x="1960" y="748">Verdalin</text>
    <text class="brand-name sleeve-brand" transform="translate(1960 1335) rotate(180)">Verdalin</text>
  </g>
</svg>
</body>
</html>
```